Flyer Design Project

We want to design a flyer for a laundromat in San Francisco. It will be used to market the services of the laundromat. I am uploading a .jpg file with details to be highlighted. The flyer should be of size 8.5 in x 11 in and should be attractive and hard hitting. The attachment should only be used for the copy, not for design.

Target Market(s)

Laundromat and laundry users

Requirements
Must have
• Must have a attention grabbing headline
Nice to have
• Pictures

```html
<!DOCTYPE html>
<html lang="en">
<head>
<meta charset="utf-8">
<title>Larkmore Laundromat Flyer</title>
<link rel="stylesheet" href="https://fonts.googleapis.com/css2?family=Arimo:wght@700&display=swap">
<style>
:root{
  --blue:#1c36d6;
  --cyan:#33d9f3;
  --cyan-soft:#bdf2fb;
  --cyan-pale:#e4fafe;
  --white:#ffffff;
}
*{margin:0;padding:0;box-sizing:border-box}
html,body{width:927px;height:1200px;overflow:hidden;background:var(--white)}
.flyer{position:relative;width:927px;height:1200px;overflow:hidden;font-family:"Arimo",Arial,sans-serif;font-weight:700;background:var(--white)}
.backdrop{position:absolute;inset:0}
.photo-area{position:absolute;left:0;top:440px;width:927px;height:650px;
  background:linear-gradient(180deg,rgba(255,255,255,0) 0%,#eef6f6 18%,#f3ece4 50%,#eaf4f6 80%,rgba(255,255,255,0) 100%)}
.headline-block{position:absolute;left:91px;top:110px;width:500px;text-align:center;color:var(--blue)}
.headline{font-size:29px;line-height:35px;margin-bottom:18px}
.services{list-style:none;font-size:26px;line-height:33.5px}
.offer{position:absolute;text-align:center;display:flex;flex-direction:column;justify-content:center;align-items:center}
.offer-free{left:656px;top:54px;width:196px;height:196px}
.offer-half{left:570px;top:406px;width:188px;height:188px}
.offer-title{color:var(--cyan);font-size:33px;line-height:36px}
.offer-text{color:var(--cyan);font-size:19px;line-height:25px;margin-top:4px}
.nearby{position:absolute;left:378px;top:538px;width:228px;height:228px;display:flex;flex-direction:column;justify-content:center;align-items:center;text-align:center;color:var(--blue);font-size:20px;line-height:25px}
.brand{position:absolute;left:0;top:0;width:927px;height:0;color:var(--blue);line-height:1}
.brand-line1{position:absolute;left:121px;top:802px;font-size:95px;letter-spacing:1px;white-space:nowrap}
.brand-line2{position:absolute;left:68px;top:912px;font-size:110px;letter-spacing:0;white-space:nowrap}
.contact{position:absolute;left:0;top:1078px;width:927px;text-align:center;color:var(--blue);font-size:20px;line-height:29px;font-style:normal}
</style>
</head>
<body>
<div class="flyer">
  <div class="photo-area" role="img" aria-label="Faded photograph of a smiling couple in front of laundromat washing machines"></div>

  <svg class="backdrop" width="927" height="1200" viewBox="0 0 927 1200" aria-hidden="true">
    <defs>
      <radialGradient id="bubble" cx="35%" cy="30%" r="75%">
        <stop offset="0" stop-color="#ffffff"/>
        <stop offset="0.45" stop-color="#c9f5fc"/>
        <stop offset="1" stop-color="#5fdff4"/>
      </radialGradient>
    </defs>
    <path d="M0 0H927V40C780 70 650 60 520 20 380 -10 200 30 0 120Z" fill="var(--cyan-pale)"/>
    <path d="M600 260C720 300 840 290 927 250V380C820 420 700 380 600 330Z" fill="var(--cyan-pale)"/>
    <circle cx="341" cy="212" r="290" fill="url(#bubble)" opacity="0.95"/>
    <circle cx="341" cy="212" r="262" fill="none" stroke="#ffffff" stroke-width="3" opacity="0.6"/>
    <circle cx="754" cy="152" r="98" fill="var(--white)" stroke="var(--cyan)" stroke-width="7" stroke-dasharray="16 9"/>
    <circle cx="664" cy="500" r="94" fill="var(--white)" stroke="var(--cyan)" stroke-width="7" stroke-dasharray="16 9"/>
    <circle cx="492" cy="652" r="114" fill="url(#bubble)"/>
    <circle cx="742" cy="712" r="83" fill="url(#bubble)"/>
    <circle cx="722" cy="320" r="42" fill="url(#bubble)"/>
    <circle cx="776" cy="362" r="34" fill="url(#bubble)"/>
    <circle cx="690" cy="368" r="26" fill="url(#bubble)"/>
    <circle cx="372" cy="490" r="40" fill="url(#bubble)"/>
    <circle cx="334" cy="530" r="28" fill="url(#bubble)"/>
    <circle cx="408" cy="536" r="24" fill="url(#bubble)"/>
    <circle cx="848" cy="1126" r="40" fill="url(#bubble)"/>
    <circle cx="882" cy="1090" r="24" fill="url(#bubble)"/>
    <circle cx="808" cy="1170" r="22" fill="url(#bubble)"/>
    <circle cx="53" cy="1160" r="18" fill="url(#bubble)"/>
  </svg>

  <div class="headline-block">
    <h1 class="headline">The Cleaniest Laundromat<br>in the Bay Area</h1>
    <ul class="services">
      <li>Large Commercial Washers</li>
      <li>Large Commercial Dryers</li>
      <li>Wash &amp; Fold Service</li>
      <li>Ample Parking</li>
      <li>WiFi</li>
      <li>Flat Screen TV</li>
    </ul>
  </div>

  <div class="offer offer-free">
    <p class="offer-title">FREE<br>WASH</p>
    <p class="offer-text">One Load of<br>20lb Wash<br>Free with This<br>Coupon</p>
  </div>

  <div class="offer offer-half">
    <p class="offer-title">50% OFF</p>
    <p class="offer-text">On Your First<br>Wash and Fold<br>Order</p>
  </div>

  <div class="nearby">
    <p>Near<br>Greenleaf Market<br>Cajun Coop<br>Jade Wok Express<br>&amp; Harbor Coffee</p>
  </div>

  <h2 class="brand">
    <span class="brand-line1">LARKMORE</span>
    <span class="brand-line2">LAUNDROMAT</span>
  </h2>

  <address class="contact">
    2280 B Larkmore Street, San Francisco, CA 94115<br>
    www.larkmorelaundromat.com<br>
    415.555.0148
  </address>
</div>
</body>
</html>
```